Press Release A BRAMBLEWICK AND A SILENT HERON book/website/on-line farmshop

I am ex-stylist.
In a few months time I will be releasing my first coffee table book/website/online farm shop. I need a short, sharp, but really beautifully pulled together and eye-pleasing one page PRESS RELEASE to send out to editors of interior and lifestyle magazines. I need to include the book cover plus publisher, a little about me, a few photographs from the book as a teaser, the new BRAMBLEWICK logo that is used on jars boxes and cartons when produce is sold, and anything else you think would make for great content within the above-mentioned publications.
I will obviously need to work with you in terms of copy to include on the page as this is quite personal. Maybe start with some of the info from the Bio and we can tweak it from there?
I will also be launching my website at the same time which will link to my own BRAMBLEWICK brand honey/eggs along with gorgeous produce boxes - available to purchase from The Bramblewick (logo attached). Need someone who can put this PRESS RELEASE together in a concise but authentic-to- my -style kind of way. Needs to look UBER clean, styled, and editorial. Have other pics and info but thought these would be a great place to start and give you an idea of the DNA of me/the book etc.

Target Market(s)

MAGAZINES

Industry/Entity Type

Lifestyle

Font styles to use
Serif

Requirements
Must have
• PRESS RELEASE ON TITLE
A BRAMBLEWICK AND A SILLENT HERON ON TITLE
Should not have
• "PROOF" ON ANY OF THE PICTURES
TWITTER, FACEBOOK OR PHONE NUMBER

```html
<!DOCTYPE html>
<html lang="en">
<head>
<meta charset="utf-8">
<title>Press Release – A Bramblewick and a Silent Heron</title>
<link rel="stylesheet" href="https://fonts.googleapis.com/css2?family=Roboto:wght@400;500;700&family=Oswald:wght@400;500&family=Sacramento&family=Tinos&display=swap">
<style>
  :root{
    --ink:#2b2b2b;
    --text:#3a3a3a;
    --white:#ffffff;
    --card:#e8e8e8;
    --accent-red:#d23a3a;
    --yellow:#f0e400;
    --cover-dark:#2a2a2a;
    --spine:#1e1e1e;
  }
  *{margin:0;padding:0;box-sizing:border-box}
  html,body{width:1200px;height:3045px;overflow:hidden;background:var(--white)}
  body{position:relative;font-family:'Roboto',Arial,sans-serif;color:var(--text)}
  .abs{position:absolute}

  .masthead{left:0;top:0;width:1200px;height:112px;background:var(--ink);
    display:flex;align-items:center;justify-content:center}
  .masthead h1{color:var(--white);font-weight:700;font-size:42px;letter-spacing:1px}

  .hero{left:0;top:112px;width:1200px;height:664px;
    background:linear-gradient(180deg,#3b3936 0%,#2c2a27 55%,#1f1d1b 100%)}
  .hero-title{left:0;top:292px;width:1200px;text-align:center;color:var(--white);
    font-weight:500;font-size:47px;line-height:60px;text-shadow:0 2px 6px rgba(0,0,0,.4)}

  .about-card{left:150px;top:610px;width:900px;height:767px;background:var(--card)}
  .portrait{left:227px;top:641px;width:318px;height:318px;border-radius:50%;
    background:radial-gradient(circle at 50% 40%,#d9d9d9,#b8b8b8 70%,#9a9a9a)}
  .intro-im{left:198px;top:982px;width:375px;text-align:center;font-size:30px;color:#333}
  .intro-name{left:198px;top:1015px;width:375px;text-align:center;
    font-family:'Sacramento',cursive;font-size:50px;color:var(--accent-red)}
  .intro-text{left:198px;top:1080px;width:375px;font-size:21px;line-height:39px;
    text-align:justify;text-align-last:center}
  .about-text{left:630px;top:662px;width:375px;font-size:21px;line-height:39px;text-align:justify}

  .book-mockup{left:45px;top:1522px;width:525px;height:586px;
    background:linear-gradient(135deg,#f2f2f2 0%,#3a3a3a 30%,#262626 70%,#4a4a4a 100%)}

  .cover-back{left:0;top:2140px;width:485px;height:785px;
    background:linear-gradient(180deg,#3d3b38,#2c2b29 60%,#232221)}
  .back-blurb{left:30px;width:425px;text-align:center;color:#eaeaea;
    font-family:'Tinos',Georgia,serif;font-size:19px;line-height:23px}
  .cover-spine{left:485px;top:2140px;width:77px;height:785px;background:var(--spine)}
  .spine-title,.spine-author{writing-mode:vertical-rl;font-family:'Oswald',sans-serif;
    color:var(--white);font-weight:500;left:507px}
  .spine-title{top:2180px;font-size:24px;letter-spacing:.5px}
  .spine-author{top:2615px;font-size:20px}
  .cover-front{left:562px;top:2140px;width:488px;height:785px;
    background:linear-gradient(180deg,#2b2b2b 0%,#5a5750 45%,#3d3a35 75%,#2a2724 100%)}
  .front-credit{left:603px;top:2337px;font-family:'Oswald',sans-serif;font-size:14px;
    letter-spacing:1.5px;color:#dcdcdc}
  .front-author{left:562px;top:2832px;width:488px;text-align:center;
    font-family:'Oswald',sans-serif;font-weight:500;font-size:42px;color:var(--white)}

  .feature{left:600px;top:1515px;width:600px;height:822px;background:var(--yellow)}
  .feature p{position:absolute;left:60px;top:45px;width:450px;font-size:21px;
    line-height:39px;text-align:justify;color:#3b3a20}

  .footer{left:0;top:2925px;width:1200px;height:120px;background:var(--ink);
    color:var(--white);display:flex;align-items:center;justify-content:center;font-size:24px}
  .footer .code{position:absolute;right:56px;font-size:20px}
</style>
</head>
<body>
  <header class="masthead abs"><h1>PRESS RELEASE</h1></header>

  <div class="hero abs" role="img" aria-label="Farmhouse kitchen interior with wooden table and chairs"></div>
  <h2 class="hero-title abs">LOREM IPSUM DOLOR SIT<br>AMET, CONSECTETUR ADIPISCING</h2>

  <section class="about-card abs"></section>
  <div class="portrait abs" role="img" aria-label="Portrait photograph of the author"></div>
  <p class="intro-im abs">I’m</p>
  <p class="intro-name abs">Tess Halloway</p>
  <p class="intro-text abs">Lorem ipsum dolor sit amet, consectetur adipiscing elit, sed do eiusmod tempor incididunt ut labore et dolore magna aliqua. Ut enim ad minim veniam, quis nostrud exercitation ullamco laboris nisi ut aliquip ex ea commodo</p>
  <p class="about-text abs">Sed ut perspiciatis unde omnis iste natus error sit voluptatem accusantium doloremque laudantium, totam rem aperiam, eaque ipsa quae ab illo inventore veritatis et quasi architecto beatae vitae dicta sunt explicabo. Nemo enim ipsam voluptatem quia voluptas sit aspernatur aut odit aut fugit, sed quia consequuntur magni dolores eos qui ratione voluptatem sequi nesciunt. Neque porro quisquam est, qui dolorem ipsum quia dolor sit amet, consectetur, adipisci velit, sed quia non numquam eius modi tempora incidunt ut labore et dolore magnam aliquam quaerat voluptatem.Ut enim ad minima veniam, quis nostrum exercitationem</p>

  <div class="book-mockup abs" role="img" aria-label="Hardcover book mockup of A Bramblewick and a Silent Heron, front and back"></div>

  <div class="cover-back abs" role="img" aria-label="Back cover photograph of a farmhouse with a horse"></div>
  <p class="back-blurb abs" style="top:2300px">An Interior Designer’s beautiful family account of a semi-rural lifestyle on the outskirts of the city of Sydney, Australia.</p>
  <p class="back-blurb abs" style="top:2418px">A pictorial tale of the lifestyle and interiors of a family farmhouse, and their community, on Sydneys Northern Beaches.</p>
  <p class="back-blurb abs" style="top:2512px">Included are poignant historical snippets of the area including a community profile on Australian of the Year, Rowan Pike, and insider information about where Wren the River Heron once called home. An inspiring way to to live and love.</p>

  <div class="cover-spine abs"></div>
  <p class="spine-title abs">A BRAMBLEWICK AND A SILENT HERON</p>
  <p class="spine-author abs">TESS HALLOWAY</p>

  <div class="cover-front abs" role="img" aria-label="Front cover photograph of a hallway with dark panelled doors and a window"></div>
  <p class="front-credit abs">WITH PHOTOGRAPHY - NED HALLOWAY &amp; IVO MARSH</p>
  <p class="front-author abs">TESS HALLOWAY</p>

  <section class="feature abs">
    <p>Sed ut perspiciatis unde omnis iste natus error sit voluptatem accusantium doloremque laudantium, totam rem aperiam, eaque ipsa quae ab illo inventore veritatis et quasi architecto beatae vitae dicta sunt explicabo. Nemo enim ipsam voluptatem quia voluptas sit aspernatur aut odit aut fugit, sed quia consequuntur magni dolores eos qui ratione voluptatem sequi nesciunt. Neque porro quisquam est, qui dolorem ipsum quia dolor sit amet, consectetur, adipisci velit, sed quia non numquam eius modi tempora incidunt ut labore et dolore magnam aliquam quaerat voluptatem. Ut enim ad minima veniam Sed ut perspiciatis unde omnis iste natus error sit voluptatem accusantium doloremque laudantium, totam rem aperiam, eaque ipsa quae ab illo inventore veritatis et quasi architecto beatae vitae dicta sunt explicabo. Nemo enim ipsam voluptatem quia voluptas</p>
  </section>

  <footer class="footer abs">Copyright © 2021. All Rights Reserved<span class="code">C38</span></footer>
</body>
</html>
```